Fresh Tarrow Work Post - Business Card Required

Dear All,

I own Velmira Limited, which in turn owns the website:
www.harbinworkpost.example

I want all of you wonderful creative people to come up with a slick, and awesome business card design that incorporates the logo on the site, and some colouring and design elements from it.

You have free reign in how you go about doing this, I won't be giving my contact details on this platform, but the winner will be asked to redesign based on my contact details which I will supply at the end.

I need the design to be completed within 5 days. I need the final print copies of the business cards by the 25th November, so unfortunately it's a bit of a rush to get these designs ready.

Any questions, please ask.

Thank you
Updates

Thank you all for your hard work and exceptional designs provided. I do have to pick one, so I have a very clear idea of which one this is, however I will wait one further day until the competition closes to be fair to all those have submitted, or are in the process of submitting. I wish you all the best and thank you again for your dedication.

```html
<!DOCTYPE html>
<html lang="en">
<head>
<meta charset="utf-8">
<title>Harbin Workpost – Business Card</title>
<link href="https://fonts.googleapis.com/css2?family=Marcellus&display=swap" rel="stylesheet">
<style>
  :root {
    --page-bg: #e9e4d8;
    --card-black: #121212;
    --card-edge: #dfe0e4;
    --gold: #c9a23a;
    --gold-dark: #a8720a;
    --brown: #8a4a12;
    --gold-mid: #d8b548;
    --gold-pale: #f3ec92;
    --panel-top: #ead676;
    --panel-bottom: #fdf8e0;
    --ink: #1c1a14;
    --ink-soft: #4a4330;
  }
  * { box-sizing: border-box; margin: 0; padding: 0; }
  html, body {
    width: 1200px; height: 1000px; overflow: hidden;
    background: var(--page-bg);
    font-family: "Marcellus", "Optima", serif;
  }
  .card {
    position: absolute; left: 220px;
    width: 760px; height: 430px;
    box-shadow: 0 6px 18px rgba(0,0,0,.25);
  }
  .card--front { top: 50px; background: var(--card-black); }
  .card--back { top: 520px; background: var(--card-edge); }

  /* brand name block */
  .brand {
    position: absolute; display: flex; flex-direction: column; align-items: center; gap: 22px;
    color: var(--gold); text-transform: uppercase; letter-spacing: 3px;
  }
  .brand__dot {
    width: 90px; height: 90px; border-radius: 50%; background: var(--gold);
  }
  .brand__name { font-size: 30px; white-space: nowrap; }
  .card--front .brand { left: 30px; width: 300px; top: 110px; letter-spacing: 2px; }
  .card--front .brand__name { font-size: 24px; }
  .card--back .brand { left: 0; right: 0; top: 105px; }
  .card--back .brand__name { font-size: 36px; }

  /* contact panel */
  .contact-panel {
    position: absolute; right: 40px; top: 40px;
    width: 350px; height: 352px; border-radius: 12px;
    background: linear-gradient(180deg, var(--panel-top), var(--panel-bottom));
    padding: 40px 30px 0 58px;
  }
  .contact-panel::before {
    content: ""; position: absolute; left: -12px; top: 176px;
    width: 24px; height: 24px; background: #f1e6a6; transform: rotate(45deg);
  }
  .person__name { font-size: 29px; color: var(--ink); letter-spacing: 1px; }
  .person__role { font-size: 14px; color: var(--ink-soft); letter-spacing: 1px; margin-top: 2px; }
  .contact-list { list-style: none; margin-top: 26px; }
  .contact-item {
    position: relative; display: flex; align-items: center; gap: 10px;
    height: 36px; margin-bottom: 6px; font-size: 13px; color: var(--ink);
  }
  .contact-item::before {
    content: ""; position: absolute; left: -28px; top: 8px;
    width: 26px; height: 22px; background: var(--gold-dark);
  }
  .contact-item__icon {
    position: relative; flex: none; width: 34px; height: 34px; border-radius: 50%;
    background: #fbf4cf; border: 3px solid var(--gold-mid);
    display: flex; align-items: center; justify-content: center;
  }
  .contact-item__text { line-height: 1.4; }

  /* back card */
  .back-field { position: absolute; left: 70px; right: 70px; top: 0; bottom: 0; background: var(--card-black); }
  .swatch-strip { position: absolute; top: 70px; width: 70px; display: flex; flex-direction: column; }
  .swatch-strip--left { left: 30px; }
  .swatch-strip--right { right: 30px; flex-direction: column-reverse; }
  .swatch { height: 75px; }
  .swatch--brown { background: var(--brown); }
  .swatch--dark { background: var(--gold-dark); }
  .swatch--mid { background: var(--gold-mid); }
  .swatch--pale { background: var(--gold-pale); }
</style>
</head>
<body>

<section class="card card--front" aria-label="Business card front">
  <div class="brand">
    <span class="brand__dot"></span>
    <span class="brand__name">Harbin Workpost</span>
  </div>

  <div class="contact-panel">
    <h1 class="person__name">IDRIS KANMORE</h1>
    <p class="person__role">MANAGING DIRECTOR</p>
    <ul class="contact-list">
      <li class="contact-item">
        <span class="contact-item__icon">
          <svg width="16" height="16" viewBox="0 0 16 16"><path d="M3 2h3l1 3-2 1c1 2 2 3 4 4l1-2 3 1v3c-6 0-10-4-10-10z" fill="#1c1a14"/></svg>
        </span>
        <span class="contact-item__text">0700 555 0148</span>
      </li>
      <li class="contact-item">
        <span class="contact-item__icon">
          <svg width="16" height="16" viewBox="0 0 16 16"><rect x="1.5" y="3.5" width="13" height="9" fill="none" stroke="#1c1a14" stroke-width="1.5"/><path d="M2 4l6 5 6-5" fill="none" stroke="#1c1a14" stroke-width="1.5"/></svg>
        </span>
        <span class="contact-item__text">contact@harbinworkpost.example</span>
      </li>
      <li class="contact-item">
        <span class="contact-item__icon">
          <svg width="16" height="16" viewBox="0 0 16 16" fill="none" stroke="#1c1a14" stroke-width="1.3"><circle cx="8" cy="8" r="6.3"/><ellipse cx="8" cy="8" rx="2.8" ry="6.3"/><path d="M1.7 8h12.6M2.8 4.8h10.4M2.8 11.2h10.4"/></svg>
        </span>
        <span class="contact-item__text">www.harbinworkpost.example</span>
      </li>
      <li class="contact-item">
        <span class="contact-item__icon">
          <svg width="16" height="16" viewBox="0 0 16 16"><path d="M8 1.5l7 6.5h-2v6.5H9.5V10h-3v4.5H3V8H1z" fill="#1c1a14"/></svg>
        </span>
        <span class="contact-item__text">17 Calder Row, Tarrow,<br>TW4 9QX</span>
      </li>
    </ul>
  </div>
</section>

<section class="card card--back" aria-label="Business card back">
  <div class="back-field"></div>
  <div class="swatch-strip swatch-strip--left">
    <span class="swatch swatch--brown"></span>
    <span class="swatch swatch--dark"></span>
    <span class="swatch swatch--mid"></span>
    <span class="swatch swatch--pale"></span>
  </div>
  <div class="swatch-strip swatch-strip--right">
    <span class="swatch swatch--brown"></span>
    <span class="swatch swatch--dark"></span>
    <span class="swatch swatch--mid"></span>
    <span class="swatch swatch--pale"></span>
  </div>
  <div class="brand">
    <span class="brand__dot"></span>
    <span class="brand__name">Harbin Workpost</span>
  </div>
</section>

</body>
</html>
```